National Virtual accounting firm needs website designed

I need a wordpress website design for a national virtual accounting firm. I will upload my business card, logo, and postcards that I have had designed and followed the same style. I want a similar style to be followed so I can keep the running theme similar.

Services include:

Tax Services:
Tax preparation and planning services for Individuals, businesses, estates, and nonprofits
Full Service Payroll for Businesses
QVT Audit Representation

Consulting:
Entity Selection & Restructuring
Financial Projections & Forecasts
Retirement Planning
IPO Readiness

Accounting:
Bookkeeping
Reviews and Compilations
Payroll Services

Other Services:
CFO Services
Compliance Services
Controller Services
Software Implementations for Tenvolk, Brombalt, and Plovena.

Target Market(s)

small to medium size businesses, and individuals

Industry/Entity Type

accounting firms

Font styles to use
Sans Serif

Colors
59FF00
82FF00
B8FF75
E3FFCB
F4FFEA

Requirements
Must have
• Color schematics from the logo and post cards/business cards

```html
<!DOCTYPE html>
<html lang="en">
<head>
<meta charset="utf-8">
<title>Vanterra — National Virtual Accounting Firm</title>
<link rel="stylesheet" href="https://fonts.googleapis.com/css2?family=Poppins:wght@300;400;500;600;700&display=swap">
<style>
:root{
  --green:#5bb53a;
  --green-light:#8cc63f;
  --green-dark:#3f9a2b;
  --yellow:#f5b800;
  --ink:#222222;
  --dark:#242424;
  --text:#333333;
  --muted:#555555;
  --grey-bg:#ececec;
  --soft-bg:#f3f3f3;
  --white:#ffffff;
}
*{box-sizing:border-box;margin:0;padding:0}
html,body{width:1200px;height:5102px;overflow:hidden}
body{font-family:"Poppins",sans-serif;color:var(--text);background:var(--white);position:relative}
.abs{position:absolute}
a{color:inherit;text-decoration:none}

/* top bar */
.topbar{position:absolute;left:0;top:0;width:1200px;height:62px}
.topbar svg{position:absolute;left:0;top:0}
.social{position:absolute;left:75px;top:22px;display:flex;gap:27px}
.social span{width:17px;height:17px;background:var(--white);border-radius:3px;display:block}
.consult{position:absolute;left:664px;top:17px;color:var(--white);font-weight:600;font-size:15px;letter-spacing:.3px}
.phone-top{position:absolute;left:920px;top:12px;color:var(--yellow);font-weight:600;font-size:22px;display:flex;align-items:center;gap:8px}

/* header */
.header{position:absolute;top:62px;left:0;width:1200px;height:92px;background:var(--white)}
.brand{position:absolute;display:flex;align-items:center;gap:10px;font-weight:400;color:var(--ink)}
.brand .dot{width:20px;height:20px;border-radius:50%;background:var(--yellow)}
.header .brand{left:80px;top:22px;font-size:38px;letter-spacing:1px}
.nav{position:absolute;right:50px;top:28px;display:flex;gap:12px;font-size:15px;color:var(--muted)}
.nav a{padding:8px 20px;border-radius:22px}
.nav a.active{background:var(--yellow);color:var(--ink);font-weight:500}

/* hero */
.hero{position:absolute;top:154px;left:0;width:1200px;height:716px;overflow:hidden}
.hero-photo{position:absolute;inset:0;background:linear-gradient(120deg,#5a6470 0%,#3c4651 40%,#2b3039 70%,#4a4f58 100%)}
.hero-shade{position:absolute;inset:0;background:rgba(20,22,28,.35)}
.hero-title{position:absolute;left:0;width:1200px;top:170px;text-align:center;color:var(--white);font-size:104px;font-weight:300;letter-spacing:6px}
.hero-sub{position:absolute;left:0;width:1200px;top:357px;text-align:center;color:var(--white);font-size:34px;font-weight:500;letter-spacing:.5px}
.btn{display:inline-block;background:var(--green);color:var(--white);font-weight:600;letter-spacing:.5px;border-radius:32px;text-align:center}
.hero .btn{position:absolute;left:481px;top:427px;width:238px;height:60px;line-height:60px;font-size:17px}
.dots{position:absolute;left:558px;top:641px;display:flex;gap:10px}
.dots span{width:14px;height:14px;border-radius:50%;background:var(--white)}
.dots span:first-child{background:var(--yellow)}
.hero svg.curve{position:absolute;left:0;bottom:0}

/* section headings */
.sec-title{position:absolute;left:0;width:1200px;text-align:center;font-size:44px;font-weight:400;color:var(--ink);letter-spacing:1px}
.swoosh{position:absolute}

/* service cards */
.card{position:absolute;width:328px;height:316px;background:var(--white);border-radius:22px;box-shadow:0 4px 22px rgba(0,0,0,.12);overflow:hidden;padding:28px 20px 0 20px}
.card .icon{width:88px;height:82px}
.card h3{font-size:20px;font-weight:600;color:var(--ink);margin-top:14px;letter-spacing:.3px}
.card p{font-size:14.5px;line-height:27px;color:var(--text);margin-top:8px}
.card .go{position:absolute;right:0;bottom:0;width:68px;height:64px;background:var(--green);border-radius:14px 0 0 0;display:flex;align-items:center;justify-content:center}

/* about */
.about{position:absolute;top:1485px;left:0;width:1200px;height:720px;overflow:hidden}
.about-bg{position:absolute;inset:0;background:linear-gradient(100deg,#2a2a2a 0%,#333 55%,#3a3a3a 100%)}
.about svg.top{position:absolute;left:0;top:0}
.about h2{position:absolute;left:75px;top:168px;color:var(--white);font-size:46px;font-weight:400;letter-spacing:1.5px}
.about p{position:absolute;left:75px;top:282px;width:520px;color:#e6e6e6;font-size:16.5px;line-height:36px}
.about .btn{position:absolute;left:75px;top:568px;width:242px;height:62px;line-height:62px;font-size:17px}
.about-ring{position:absolute;left:633px;top:165px;width:496px;height:496px;border-radius:50%;border:9px solid var(--yellow);background:#1a1a1a;padding:10px}
.about-photo{width:100%;height:100%;border-radius:50%;background:linear-gradient(135deg,#d9dde2 0%,#8d96a0 45%,#3b4652 100%)}

/* testimonials */
.testi{position:absolute;top:2798px;left:0;width:1200px;height:974px;background:var(--grey-bg);overflow:hidden}
.testi svg.band{position:absolute;left:0;top:310px}
.quote-card{position:absolute;left:253px;top:188px;width:692px;height:400px;border-radius:24px;background:linear-gradient(180deg,#8cc63f 0%,#4caf50 100%);text-align:center;color:var(--white)}
.avatar{position:absolute;left:291px;top:26px;width:110px;height:110px;border-radius:50%;background:linear-gradient(135deg,#c9c9c9,#6d6d6d);border:3px solid var(--white)}
.quote-card p{position:absolute;left:36px;top:162px;width:620px;font-size:15.5px;line-height:29px}
.quote-card h4{position:absolute;left:0;width:692px;top:320px;font-size:16px;font-weight:500}
.stars{position:absolute;left:292px;top:350px;display:flex;gap:7px}
.arrow-nav{position:absolute;top:370px}
.why{position:absolute;left:75px;top:653px;width:1052px;height:228px;border-radius:26px;background:linear-gradient(100deg,#2f3b45 0%,#3f4d58 50%,#2b3640 100%);overflow:hidden}
.why h2{position:absolute;left:33px;top:44px;color:var(--white);font-size:44px;font-weight:400;line-height:44px;letter-spacing:1px}
.why .item{position:absolute;top:50px;width:220px;text-align:center;color:var(--white);font-weight:600;font-size:20px;letter-spacing:.5px}
.why .item .ic{width:90px;height:90px;border-radius:50%;background:var(--yellow);margin:0 auto 18px;display:flex;align-items:center;justify-content:center}
.why .sep{position:absolute;top:52px;width:1px;height:128px;background:rgba(255,255,255,.35)}

/* news */
.news{position:absolute;top:3772px;left:0;width:1200px;height:760px;background:var(--soft-bg)}
.news h2{position:absolute;left:72px;top:52px;font-size:44px;font-weight:400;color:var(--ink);letter-spacing:1px}
.post{position:absolute;top:174px;width:328px;height:470px;background:var(--white);border-radius:22px;box-shadow:0 4px 22px rgba(0,0,0,.1);overflow:hidden}
.post .img{height:228px}
.post .body{padding:26px 20px 0 20px}
.post .date{color:var(--green);font-size:15px;font-weight:500}
.post h3{font-size:21px;font-weight:500;line-height:29px;color:var(--ink);margin-top:8px}
.post p{font-size:14.5px;line-height:26px;margin-top:8px;color:var(--text)}
.post .go{position:absolute;left:26px;bottom:24px;width:34px;height:34px;border-radius:50%;background:var(--green);display:flex;align-items:center;justify-content:center}

/* footer */
.footer{position:absolute;top:4505px;left:0;width:1200px;height:597px;overflow:hidden}
.footer svg.top{position:absolute;left:0;top:0}
.footer-bg{position:absolute;left:0;top:60px;width:1200px;height:537px;background:#1d1d1d}
.footer .brand{left:0;width:1200px;justify-content:center;top:72px;font-size:42px;color:var(--white);letter-spacing:1.5px}
.fcol{position:absolute;top:218px}
.fcol h4{color:var(--green);font-size:16px;font-weight:500;letter-spacing:.5px;margin-bottom:10px}
.fcol li{list-style:none;color:#cfcfcf;font-size:14.5px;line-height:36px}
.fcol .line{color:#cfcfcf;font-size:14.5px;line-height:27px}
.fsocial{display:flex;gap:28px;margin-top:22px}
.fsocial span{width:17px;height:17px;background:var(--yellow);border-radius:3px;display:block}
.map{position:absolute;left:794px;top:217px;width:333px;height:252px;border-radius:22px;background:linear-gradient(160deg,#f1f1ee 0%,#e4e6e1 100%);border:4px solid var(--white)}
.copy{position:absolute;left:0;bottom:0;width:1200px;height:63px;background:#141414;color:#bdbdbd;font-size:13px;text-align:center;line-height:63px}
</style>
</head>
<body>

<!-- top bar -->
<div class="topbar">
  <svg width="1200" height="62" viewBox="0 0 1200 62">
    <rect width="1200" height="62" fill="#5bb53a"/>
    <polygon points="650,0 1200,0 1200,62 620,62" fill="#222"/>
    <polygon points="636,0 650,0 620,62 606,62" fill="#8cc63f"/>
  </svg>
  <div class="social"><span></span><span></span><span></span><span></span></div>
  <div class="consult">SCHEDULE A FREE CONSULT</div>
  <div class="phone-top">
    <svg width="18" height="18" viewBox="0 0 24 24"><path d="M6.6 10.8a15 15 0 0 0 6.6 6.6l2.2-2.2a1 1 0 0 1 1-.25 11.4 11.4 0 0 0 3.6.57 1 1 0 0 1 1 1V20a1 1 0 0 1-1 1A17 17 0 0 1 3 4a1 1 0 0 1 1-1h3.5a1 1 0 0 1 1 1c0 1.25.2 2.45.57 3.6a1 1 0 0 1-.25 1z" fill="#f5b800"/></svg>
    (800) 555-0147
  </div>
</div>

<!-- header -->
<header class="header">
  <div class="brand"><span class="dot"></span>VANTERRA</div>
  <nav class="nav">
    <a class="active" href="#">Home</a><a href="#">About Us</a><a href="#">Services</a><a href="#">Testimonials</a><a href="#">News</a><a href="#">Contact Us</a>
  </nav>
</header>

<!-- hero -->
<section class="hero">
  <div class="hero-photo" role="img" aria-label="Business people reviewing financial charts and reports at a desk"></div>
  <div class="hero-shade"></div>
  <h1 class="hero-title">VANTERRA</h1>
  <div class="hero-sub">WE ARE A NATIONAL VIRTUAL ACCOUNTING FIRM</div>
  <a class="btn" href="#">READ MORE</a>
  <div class="dots"><span></span><span></span><span></span><span></span></div>
  <svg class="curve" width="1200" height="110" viewBox="0 0 1200 110" preserveAspectRatio="none">
    <path d="M0,42 Q600,140 1200,0 L1200,110 L0,110 Z" fill="#5bb53a"/>
    <path d="M0,70 Q600,150 1200,30 L1200,110 L0,110 Z" fill="#ffffff"/>
  </svg>
</section>

<!-- our services -->
<h2 class="sec-title" style="top:952px">OUR SERVICES</h2>
<svg class="swoosh" style="left:488px;top:1016px" width="224" height="24" viewBox="0 0 224 24"><path d="M2,22 Q100,-6 222,16 Q110,4 2,22Z" fill="#5bb53a"/></svg>

<div class="card" style="left:75px;top:1075px">
  <svg class="icon" viewBox="0 0 88 82" fill="none" stroke="#5bb53a" stroke-width="2.5"><rect x="30" y="4" width="50" height="66" rx="3"/><path d="M38 28h34M38 38h34M38 48h24"/><rect x="4" y="30" width="34" height="48" rx="3" fill="#fff"/><path d="M10 38h22M10 50h6M20 50h6M10 60h6M20 60h6M10 70h6M20 70h6"/><text x="52" y="20" fill="#5bb53a" stroke="none" font-family="Poppins,sans-serif" font-size="13">TAX</text></svg>
  <h3>TAX SERVICES</h3>
  <p>Expert guidance, maximum refunds, timely filling, and peace of mind. Our tax services are reliable for both Individuals and Businesses.</p>
  <div class="go"><svg width="28" height="28" viewBox="0 0 24 24"><path d="M4 12h14M12 5l7 7-7 7" stroke="#fff" stroke-width="3" fill="none"/></svg></div>
</div>
<div class="card" style="left:436px;top:1075px">
  <svg class="icon" viewBox="0 0 88 82" fill="none" stroke="#5bb53a" stroke-width="2.5"><circle cx="20" cy="30" r="8"/><circle cx="66" cy="30" r="8"/><path d="M8 76V52a12 12 0 0 1 24 0v24M54 76V52a12 12 0 0 1 24 0v24M30 58h26"/><rect x="28" y="4" width="14" height="12" rx="2"/><rect x="46" y="4" width="14" height="12" rx="2"/></svg>
  <h3>CONSULTING</h3>
  <p>Expert guidance, maximum refunds, timely filling, and peace of mind. Our tax services are reliable for both Individuals and Businesses.</p>
  <div class="go"><svg width="28" height="28" viewBox="0 0 24 24"><path d="M4 12h14M12 5l7 7-7 7" stroke="#fff" stroke-width="3" fill="none"/></svg></div>
</div>
<div class="card" style="left:798px;top:1075px">
  <svg class="icon" viewBox="0 0 88 82" fill="none" stroke="#5bb53a" stroke-width="2.5"><rect x="4" y="4" width="34" height="44" rx="3"/><path d="M10 12h22M10 22h6M20 22h6M10 32h6M20 32h6"/><rect x="30" y="20" width="40" height="56" rx="3" fill="#fff"/><circle cx="44" cy="58" r="9"/><path d="M50 32h14M50 40h14M76 30 58 60"/></svg>
  <h3>ACCOUNTING</h3>
  <p>Expert guidance, maximum refunds, timely filling, and peace of mind. Our tax services are reliable for both Individuals and Businesses.</p>
  <div class="go"><svg width="28" height="28" viewBox="0 0 24 24"><path d="M4 12h14M12 5l7 7-7 7" stroke="#fff" stroke-width="3" fill="none"/></svg></div>
</div>

<!-- about -->
<section class="about">
  <div class="about-bg" role="img" aria-label="Dark office backdrop"></div>
  <svg class="top" width="1200" height="120" viewBox="0 0 1200 120" preserveAspectRatio="none">
    <path d="M0,0 H1200 V100 Q600,-40 0,100 Z" fill="#ffffff"/>
    <path d="M0,100 Q600,-40 1200,100 L1200,120 Q600,10 0,120 Z" fill="#5bb53a"/>
  </svg>
  <h2>ABOUT VANTERRA</h2>
  <p>Sed ut perspiciatis unde omnis iste natus error sit voluptatem accusantium doloremque laudantium, totam rem aperiam, eaque ipsa quae ab illo inventore veritatis et quasi architecto beatae vitae dicta sunt explicabemo enim ipsam voluptatem quia voluptas sit aspernatur aut odit aut fugit, sed quia consequuntur magni dolores eos qui ratione voluptatem sequi nesciunt.</p>
  <a class="btn" href="#">READ MORE</a>
  <div class="about-ring"><div class="about-photo" role="img" aria-label="Two smiling businessmen shaking hands in an office"></div></div>
</section>

<!-- other services -->
<h2 class="sec-title" style="top:2265px">OTHER SERVICES</h2>
<svg class="swoosh" style="left:488px;top:2330px" width="224" height="24" viewBox="0 0 224 24"><path d="M2,22 Q100,-6 222,16 Q110,4 2,22Z" fill="#5bb53a"/></svg>

<div class="card" style="left:75px;top:2388px">
  <svg class="icon" viewBox="0 0 88 82" fill="none" stroke="#5bb53a" stroke-width="2.5"><circle cx="36" cy="18" r="10"/><path d="M18 52a18 18 0 0 1 36 0"/><rect x="6" y="52" width="60" height="20" rx="2"/><path d="M2 76h68"/></svg>
  <h3>CFO SERVICES</h3>
  <p>Expert financial advice, strategic financial planning, budgeting and forecasting, and cash flow mangement to optimize.</p>
  <div class="go"><svg width="28" height="28" viewBox="0 0 24 24"><path d="M4 12h14M12 5l7 7-7 7" stroke="#fff" stroke-width="3" fill="none"/></svg></div>
</div>
<div class="card" style="left:436px;top:2388px">
  <svg class="icon" viewBox="0 0 88 82" fill="none" stroke="#5bb53a" stroke-width="2.5"><rect x="6" y="6" width="44" height="66" rx="3"/><path d="M14 22h4M24 22h18M14 36h4M24 36h18M14 50h4M24 50h12"/><circle cx="54" cy="62" r="11" fill="#fff"/><path d="M49 62l4 4 7-8"/></svg>
  <h3>COMPLIANCE SERVICES</h3>
  <p>Expert guidance, maximum refunds, timely filling, and peace of mind. Our tax services are reliable for both Individuals and Businesses.</p>
  <div class="go"><svg width="28" height="28" viewBox="0 0 24 24"><path d="M4 12h14M12 5l7 7-7 7" stroke="#fff" stroke-width="3" fill="none"/></svg></div>
</div>
<div class="card" style="left:798px;top:2388px">
  <svg class="icon" viewBox="0 0 88 82" fill="none" stroke="#5bb53a" stroke-width="2.5"><rect x="4" y="4" width="76" height="70" rx="4"/><path d="M4 22h76M16 34v30M30 34v30M44 34v30M58 34v30M70 34v30"/><circle cx="16" cy="46" r="4" fill="#fff"/><circle cx="30" cy="54" r="4" fill="#fff"/><circle cx="44" cy="42" r="4" fill="#fff"/><circle cx="58" cy="50" r="4" fill="#fff"/><circle cx="70" cy="44" r="4" fill="#fff"/></svg>
  <h3>CONTROLLER SERVICES</h3>
  <p>Expert guidance, maximum refunds, timely filling, and peace of mind. Our tax services are reliable for both Individuals and Businesses.</p>
  <div class="go"><svg width="28" height="28" viewBox="0 0 24 24"><path d="M4 12h14M12 5l7 7-7 7" stroke="#fff" stroke-width="3" fill="none"/></svg></div>
</div>

<!-- testimonials + why choose us -->
<section class="testi">
  <svg class="band" width="1200" height="160" viewBox="0 0 1200 160" preserveAspectRatio="none">
    <path d="M0,0 Q300,60 600,70 T1200,40 L1200,58 Q900,100 600,92 Q300,80 0,44Z" fill="#5bb53a"/>
  </svg>
  <h2 class="sec-title" style="top:62px">WHAT OUR CLIENT SAYS</h2>
  <svg class="swoosh" style="left:488px;top:126px" width="224" height="24" viewBox="0 0 224 24"><path d="M2,22 Q100,-6 222,16 Q110,4 2,22Z" fill="#5bb53a"/></svg>
  <svg class="arrow-nav" style="left:204px" width="22" height="40" viewBox="0 0 22 40"><path d="M19 2 3 20l16 18" stroke="#333" stroke-width="3" fill="none"/></svg>
  <svg class="arrow-nav" style="left:974px" width="22" height="40" viewBox="0 0 22 40"><path d="M3 2l16 18L3 38" stroke="#333" stroke-width="3" fill="none"/></svg>
  <div class="quote-card">
    <div class="avatar" role="img" aria-label="Client portrait"></div>
    <p>" Sed ut perspiciatis unde omnis iste natus error sit voluptatem accusantium doloremque laudantium, totam rem aperiam, eaque ipsa quae ab illo inventore veritatis et quasi architecto beatae vitae dicta sunt explicabemo enim ipsam voluptatem quia voluptas sit aspernatur aut odit aut fugit, sed quia consequuntur.."</p>
    <h4>NAME HEADING</h4>
    <div class="stars">
      <svg width="18" height="18" viewBox="0 0 24 24"><path d="M12 2l3 7 7 .6-5.3 4.6L18.4 22 12 18l-6.4 4 1.7-7.8L2 9.6 9 9z" fill="#f5d000"/></svg>
      <svg width="18" height="18" viewBox="0 0 24 24"><path d="M12 2l3 7 7 .6-5.3 4.6L18.4 22 12 18l-6.4 4 1.7-7.8L2 9.6 9 9z" fill="#f5d000"/></svg>
      <svg width="18" height="18" viewBox="0 0 24 24"><path d="M12 2l3 7 7 .6-5.3 4.6L18.4 22 12 18l-6.4 4 1.7-7.8L2 9.6 9 9z" fill="#f5d000"/></svg>
      <svg width="18" height="18" viewBox="0 0 24 24"><path d="M12 2l3 7 7 .6-5.3 4.6L18.4 22 12 18l-6.4 4 1.7-7.8L2 9.6 9 9z" fill="#f5d000"/></svg>
      <svg width="18" height="18" viewBox="0 0 24 24"><path d="M12 2l3 7 7 .6-5.3 4.6L18.4 22 12 18l-6.4 4 1.7-7.8L2 9.6 9 9z" fill="#f5d000"/></svg>
    </div>
  </div>

  <div class="why">
    <h2>WHY<br>CHOOSE US</h2>
    <svg class="abs" style="left:33px;top:148px" width="230" height="20" viewBox="0 0 230 20"><path d="M2,18 Q110,-6 228,14 Q110,4 2,18Z" fill="#5bb53a"/></svg>
    <div class="item" style="left:328px">
      <div class="ic"><svg width="44" height="44" viewBox="0 0 24 24" fill="none" stroke="#333" stroke-width="1.6"><circle cx="12" cy="9" r="6"/><path d="M8 14l-2 8 6-3 6 3-2-8"/></svg></div>EXPIRIENCED
    </div>
    <div class="sep" style="left:548px"></div>
    <div class="item" style="left:568px">
      <div class="ic"><svg width="44" height="44" viewBox="0 0 24 24" fill="none" stroke="#333" stroke-width="1.6"><circle cx="12" cy="7" r="4"/><path d="M4 22a8 8 0 0 1 16 0"/></svg></div>PROFESSIONAL
    </div>
    <div class="sep" style="left:806px"></div>
    <div class="item" style="left:818px">
      <div class="ic"><svg width="44" height="44" viewBox="0 0 24 24" fill="none" stroke="#333" stroke-width="1.6"><circle cx="12" cy="12" r="8"/><path d="M14.5 9a2.5 2 0 0 0-5 0c0 2.5 5 1.5 5 4a2.5 2 0 0 1-5 0M12 5.5v13"/></svg></div>AFFORDABLE
    </div>
  </div>
</section>

<!-- news -->
<section class="news">
  <h2>LATEST NEWS</h2>
  <svg class="abs" style="left:72px;top:118px" width="224" height="24" viewBox="0 0 224 24"><path d="M2,22 Q100,-6 222,16 Q110,4 2,22Z" fill="#5bb53a"/></svg>
  <article class="post" style="left:75px">
    <div class="img" role="img" aria-label="Laptop showing financial charts on a desk" style="background:linear-gradient(135deg,#9aa3ab,#3d4650)"></div>
    <div class="body"><div class="date">July 18, 2023</div><h3>Excepteur sint occaeca cupidatat non</h3><p>Nemo enim ipsam voluptatem quia voluptas sit aspernatur aut odit aut fugit, sed quia consequuntur</p></div>
    <div class="go"><svg width="18" height="18" viewBox="0 0 24 24"><path d="M4 12h14M12 5l7 7-7 7" stroke="#fff" stroke-width="3" fill="none"/></svg></div>
  </article>
  <article class="post" style="left:436px">
    <div class="img" role="img" aria-label="Senior couple meeting with a financial advisor" style="background:linear-gradient(135deg,#d2cabd,#6f6a62)"></div>
    <div class="body"><div class="date">July 18, 2023</div><h3>Excepteur sint occaeca cupidatat non</h3><p>Nemo enim ipsam voluptatem quia voluptas sit aspernatur aut odit aut fugit, sed quia consequuntur</p></div>
    <div class="go"><svg width="18" height="18" viewBox="0 0 24 24"><path d="M4 12h14M12 5l7 7-7 7" stroke="#fff" stroke-width="3" fill="none"/></svg></div>
  </article>
  <article class="post" style="left:798px">
    <div class="img" role="img" aria-label="Payroll concept with calculator and glasses" style="background:linear-gradient(135deg,#7d858d,#2e353c)"></div>
    <div class="body"><div class="date">July 18, 2023</div><h3>Excepteur sint occaeca cupidatat non</h3><p>Nemo enim ipsam voluptatem quia voluptas sit aspernatur aut odit aut fugit, sed quia consequuntur</p></div>
    <div class="go"><svg width="18" height="18" viewBox="0 0 24 24"><path d="M4 12h14M12 5l7 7-7 7" stroke="#fff" stroke-width="3" fill="none"/></svg></div>
  </article>
</section>

<!-- footer -->
<footer class="footer">
  <svg class="top" width="1200" height="120" viewBox="0 0 1200 120" preserveAspectRatio="none">
    <rect width="1200" height="120" fill="#f3f3f3"/>
    <path d="M0,70 Q600,-20 1200,70 L1200,120 L0,120Z" fill="#5bb53a"/>
    <path d="M0,96 Q600,0 1200,96 L1200,120 L0,120Z" fill="#1d1d1d"/>
  </svg>
  <div class="footer-bg"></div>
  <div class="brand"><span class="dot"></span>VANTERRA</div>
  <div class="fcol" style="left:75px"><h4>SITE MAP</h4><ul><li>Home</li><li>About Us</li><li>Services</li><li>Testimonials</li><li>News</li><li>Contact Us</li></ul></div>
  <div class="fcol" style="left:302px"><h4>SERVICES</h4><ul><li>Tax Services</li><li>Consulting</li><li>Accounting</li><li>Other Services</li></ul></div>
  <div class="fcol" style="left:525px"><h4>CONTACT INFO</h4>
    <div class="line">P.O. Box 4410<br>Ridgeview, MT 59000</div>
    <div class="line" style="margin-top:10px">(800) 555-0147</div>
    <div class="line" style="margin-top:10px">info@vanterra-mail.com</div>
    <div class="fsocial"><span></span><span></span><span></span><span></span></div>
  </div>
  <div class="map" role="img" aria-label="Street map showing the office location"></div>
  <div class="copy">Copyright © 2023 Company Name. All Right Reserved</div>
</footer>

</body>
</html>
```